Company Values One-Pager

We're a recruitment firm based in Singapore, focused on the startup tech and VC sectors. www.brelvanhire.com

As we're now at the point of growing and hiring, we want a one-pager (PDF or whatever) that summarises us and our company values.

I've attached a short PowerPoint that goes into the values etc.

Font styles to use
Sans Serif

Requirements
Must have
• We like a 'clean' look. Our logo is bright and simple, and that's what we're looking for.
• The official colour code for the logo is seafoam green
• www.huepondlab.com/color/71EEB8/sea_foam_green
• Our website also gives a good insight.
• I'd like logos that summarise each value alongside them. i.e + for positivity, a letter for delivery etc. (Just ideas - please innovate!)
Should not have
• Nothing dark - just keep it simple and fresh

```html
<!DOCTYPE html>
<html lang="en">
<head>
<meta charset="utf-8">
<title>Brelvan Hire – Company Values</title>
<link rel="stylesheet" href="https://fonts.googleapis.com/css2?family=Open+Sans:wght@300;400;600;700&display=swap">
<style>
  :root {
    --seafoam: #69e2a8;
    --ink: #8a8a8c;
    --slate: #98999b;
    --paper: #ffffff;
    --backdrop: #c9cbca;
  }
  * { margin: 0; padding: 0; box-sizing: border-box; }
  html, body {
    width: 1200px; height: 1200px; overflow: hidden;
    background: var(--backdrop);
    font-family: "Open Sans", Arial, sans-serif;
  }
  .sheet {
    position: absolute; left: 193px; top: 21px;
    width: 814px; height: 1157px;
    background: var(--paper); overflow: hidden;
  }
  .band { position: absolute; left: 0; width: 100%; height: 12px; background: var(--seafoam); }
  .band--top { top: 0; }
  .band--bottom { top: 1145px; }

  .brand {
    position: absolute; left: 40px; top: 70px;
    color: var(--seafoam); font-weight: 600;
    font-size: 40px; line-height: 1.05; letter-spacing: 4px;
  }

  .founders {
    position: absolute; left: 453px; top: 37px; width: 361px; height: 137px;
    background: var(--seafoam); color: var(--paper);
    padding: 8px 0 0 49px;
  }
  .founders__label { font-size: 17px; font-weight: 600; line-height: 24px; }
  .founder { display: flex; align-items: center; height: 44px; margin-top: 1px; }
  .founder__photo {
    width: 38px; height: 38px; border-radius: 50%;
    background: radial-gradient(circle at 50% 40%, #d9cfc6, #8b8f94);
    border: 2px solid var(--paper); flex: none;
  }
  .founder__name { margin-left: 17px; font-size: 33px; font-weight: 600; }

  .tagline {
    position: absolute; left: 43px; top: 218px;
    font-size: 24px; font-weight: 600; color: var(--ink);
  }

  .fact { position: absolute; left: 62px; width: 686px; text-align: center; }
  .fact__title {
    display: flex; align-items: center; gap: 10px;
    font-size: 34px; font-weight: 600; color: var(--ink); line-height: 40px;
  }
  .fact__title::before, .fact__title::after {
    content: ""; flex: 1; height: 3px; background: var(--seafoam);
  }
  .fact__detail { font-size: 30px; color: var(--seafoam); line-height: 40px; margin-top: 2px; }
  .fact--opened { top: 307px; }
  .fact--goal { top: 402px; }
  .fact--values { top: 491px; }
  .fact--values .fact__title { gap: 28px; }

  .value-chain { position: absolute; left: 0; top: 0; }

  .value { position: absolute; width: 230px; }
  .value__name {
    font-size: 17px; font-weight: 600; color: var(--seafoam);
    line-height: 22px; border-bottom: 1.5px solid var(--seafoam); width: 218px;
  }
  .value__text { font-size: 17px; font-weight: 300; color: var(--ink); line-height: 24px; margin-top: 4px; width: 340px; }
  .value--positivity { left: 41px; top: 748px; }
  .value--proactivity { left: 41px; top: 853px; }
  .value--teamwork { left: 387px; top: 776px; }
  .value--teamwork .value__text { margin-top: 8px; }
  .value--delivery { left: 387px; top: 882px; }
  .value--delivery .value__text { margin-top: 8px; width: 400px; }

  .contact {
    position: absolute; left: 319px; top: 986px; width: 495px; height: 135px;
    background: var(--slate); color: var(--paper);
    padding: 21px 0 0 68px;
    font-size: 17px; font-weight: 600; line-height: 23.8px;
  }
  .pitch {
    position: absolute; left: 0; top: 922px; width: 369px; height: 179px;
    background: var(--seafoam); color: var(--paper);
    padding: 23px 0 0 35px;
    font-size: 19px; font-weight: 600; line-height: 26.5px;
  }
</style>
</head>
<body>
<main class="sheet">
  <div class="band band--top"></div>

  <div class="brand">BRELVAN<br>HIRE</div>

  <section class="founders">
    <p class="founders__label">Established by</p>
    <div class="founder">
      <span class="founder__photo" role="img" aria-label="Portrait photo of co-founder Daren Loke"></span>
      <span class="founder__name">Daren Loke &amp;</span>
    </div>
    <div class="founder">
      <span class="founder__photo" role="img" aria-label="Portrait photo of co-founder Owen Tasker"></span>
      <span class="founder__name">Owen Tasker</span>
    </div>
  </section>

  <p class="tagline">‘Partner to the Startup Ecosystem’</p>

  <section class="fact fact--opened">
    <h2 class="fact__title">OPENED OUR DOORS</h2>
    <p class="fact__detail">in September 2016</p>
  </section>
  <section class="fact fact--goal">
    <h2 class="fact__title">LONGER-TERM GOAL</h2>
    <p class="fact__detail">Asia and Global expansion</p>
  </section>
  <section class="fact fact--values">
    <h2 class="fact__title">CORE VALUES</h2>
  </section>

  <svg class="value-chain" width="814" height="760" viewBox="0 0 814 760">
    <g fill="none" stroke="#69e2a8" stroke-width="4.5">
      <circle cx="101" cy="639" r="59"/>
      <circle cx="305" cy="639" r="59"/>
      <circle cx="509" cy="639" r="59"/>
      <circle cx="712" cy="639" r="59"/>
      <line x1="184" y1="639" x2="225" y2="639"/>
      <line x1="386" y1="639" x2="427" y2="639"/>
      <line x1="591" y1="639" x2="632" y2="639"/>
    </g>
    <g fill="#8a8a8c" font-family="Open Sans, Arial, sans-serif" font-size="24" font-weight="400" text-anchor="middle">
      <text x="101" y="647">Positivity</text>
      <text x="305" y="647">Proactivity</text>
      <text x="509" y="651">Teamwork</text>
      <text x="712" y="647">Delivery</text>
    </g>
  </svg>

  <div class="value value--positivity">
    <h3 class="value__name">Positivity</h3>
    <p class="value__text">We look on the bright side… and don’t let limiting beliefs hold us back</p>
  </div>
  <div class="value value--proactivity">
    <h3 class="value__name">Proactivity</h3>
    <p class="value__text">We don't wait… we make things happen</p>
  </div>
  <div class="value value--teamwork">
    <h3 class="value__name">Teamwork</h3>
    <p class="value__text">We work together… to solve problems,<br>find solutions, and celebrate the good times</p>
  </div>
  <div class="value value--delivery">
    <h3 class="value__name">Delivery</h3>
    <p class="value__text">We do what we say we're going to do…<br>for our candidates, clients, and colleagues alike</p>
  </div>

  <address class="contact" style="font-style:normal">
    Brelvan Hire Pte. Ltd. (EA No. 19X4072)<br>
    48 Marlow Road, Tidewell House, Singapore 078213<br>
    +65 6480 2735<br>
    hello@brelvanhire.com
  </address>

  <p class="pitch">We are the ‘recruitment partner<br>for the startup ecosystem in<br>South-East Asia’; partnering<br>with Venture Capital and startup<br>tech firms, HQ’d out of Singapore.</p>

  <div class="band band--bottom"></div>
</main>
</body>
</html>
```